Brinewardsea.com Website design needed!!

We are looking for a website layout to match the attached logo. We specialize in Dive Charters and currently are located in the Virgin Islands off of St. Thomas. Please create a design that is compatible with Bootstrap and have the grid in mind. WE are looking for creative and extremely professional layout design.

Target Market(s)

Scuba Diving, Divers looking for a diving charter in the Virgin Islands.

Number of Pages Required

3 page

Font styles to use
Serif

Requirements
Must have
• Must be Bootstrap friendly.
• Must work with the logo we provided. Colors etc.

```html
<!DOCTYPE html>
<html lang="en">
<head>
<meta charset="utf-8">
<title>Brinewardsea.com — Dive Charters</title>
<link href="https://fonts.googleapis.com/css2?family=Lato:wght@100;300;400;700;900&display=swap" rel="stylesheet">
<style>
:root{
  --red:#e31b23;
  --ink:#222222;
  --footer:#1c1c1c;
  --grey-bg:#ececec;
  --grey-text:#9a9a9a;
  --footer-text:#5c5c5c;
  --white:#ffffff;
  --sea-deep:#0b2f42;
  --sea-mid:#1d6a85;
  --sea-light:#5fb8d2;
  --reef:#b8743a;
}
*{box-sizing:border-box;margin:0;padding:0}
html,body{width:1200px;height:3789px;overflow:hidden}
body{position:relative;font-family:'Lato',sans-serif;color:var(--white);background:var(--footer)}
.layer{position:absolute;left:0;width:1200px}
p{font-size:15px;line-height:24px}

/* hero */
.hero-photo{top:0;height:470px;background:
  radial-gradient(ellipse 380px 120px at 640px 250px,rgba(255,255,255,.28),transparent 70%),
  radial-gradient(ellipse 520px 200px at 880px 120px,rgba(120,210,230,.45),transparent 70%),
  radial-gradient(ellipse 600px 240px at 200px 380px,rgba(8,40,60,.6),transparent 70%),
  repeating-linear-gradient(115deg,rgba(255,255,255,.05) 0 14px,transparent 14px 46px),
  linear-gradient(170deg,#0e4e66 0%,#2a8fb0 38%,#1b6f8c 62%,#0c3a50 100%)}
.site-header{position:absolute;top:0;left:0;width:1200px;height:120px;z-index:20}
.brand{position:absolute;left:50px;top:32px;width:142px;height:64px;background:var(--white);display:flex;align-items:center;justify-content:center;font-weight:700;font-size:16px;color:var(--red)}
.main-nav{position:absolute;right:50px;top:62px;display:flex;gap:32px}
.main-nav a{color:var(--white);font-weight:700;font-size:17px;text-decoration:none;letter-spacing:.3px;position:relative}
.main-nav a.active{color:var(--red)}
.main-nav a.hover-mark::after{content:"";position:absolute;left:50%;bottom:-9px;width:4px;height:4px;margin-left:-2px;background:var(--white);border-radius:50%}
.slider-arrows{position:absolute;top:452px;left:1088px;z-index:20;display:flex;gap:18px}

/* intro red band */
.intro{top:430px;height:640px;background:var(--red);clip-path:polygon(0 5px,100% 45px,100% 510px,0 631px);z-index:5}
.intro h1{position:absolute;left:50px;top:100px;font-size:66px;line-height:72px;letter-spacing:1px}
.intro h1 .thin{font-weight:100;display:block}
.intro h1 .bold{font-weight:900;display:block;font-size:68px}
.intro .col{position:absolute;top:265px;width:540px}
.col-left{left:50px}.col-right{left:614px}
.btn{position:absolute;display:flex;align-items:center;justify-content:center;width:215px;height:63px;font-weight:700;font-size:19px;color:var(--white)}
.btn-dark{background:var(--ink);left:50px;top:431px}
.btn-red{background:var(--red)}

/* about */
.about-photo{top:900px;height:860px;background:
  radial-gradient(ellipse 500px 160px at 900px 120px,rgba(140,215,235,.35),transparent 70%),
  radial-gradient(ellipse 300px 200px at 1050px 560px,rgba(60,120,90,.45),transparent 70%),
  radial-gradient(ellipse 260px 160px at 480px 520px,rgba(10,40,60,.5),transparent 70%),
  repeating-linear-gradient(100deg,rgba(255,255,255,.04) 0 10px,transparent 10px 60px),
  linear-gradient(180deg,#2c86a8 0%,#1a5f7e 40%,#103f57 75%,#0c3146 100%)}
.about-dark{top:1640px;height:120px;background:var(--ink);clip-path:polygon(0 0,100% 40px,100% 120px,0 120px);z-index:2}
.about{top:1060px;height:600px;z-index:6}
.section-title{font-size:72px;line-height:80px;font-weight:900;letter-spacing:1px}
.section-title .thin{font-weight:100}
.about .section-title{position:absolute;right:50px;top:24px;text-align:right}
.feature{position:absolute;width:540px;height:160px}
.feature .num{position:absolute;left:0;top:0;width:132px;height:132px;border-radius:50%;background:var(--red);display:flex;align-items:center;justify-content:center;font-size:56px;font-weight:700}
.feature h3{position:absolute;left:160px;top:-8px;width:370px;font-size:22px;line-height:28px;font-weight:900}
.feature p{position:absolute;left:160px;top:60px;width:370px;font-size:14px;line-height:23px}
.f1{left:50px;top:182px}.f2{left:614px;top:182px}.f3{left:50px;top:393px}.f4{left:614px;top:393px}

/* events */
.events{top:1690px;height:750px;background:var(--grey-bg);clip-path:polygon(0 55px,100% 0,100% 750px,0 695px);z-index:4;color:var(--ink)}
.events .section-title{position:absolute;left:50px;top:97px;color:var(--ink)}
.event{position:absolute;top:210px;width:340px;text-align:center}
.event .photo{width:285px;height:285px;border-radius:50%;margin:0 auto}
.photo-surface{background:
  radial-gradient(circle at 30% 25%,rgba(255,255,255,.45),transparent 35%),
  linear-gradient(180deg,#5cc0df 0%,#1f7ea6 45%,#0d3f6a 100%)}
.photo-reef{background:
  radial-gradient(ellipse 160px 70px at 50% 95%,var(--reef),transparent 75%),
  radial-gradient(circle at 55% 20%,rgba(190,235,245,.6),transparent 40%),
  linear-gradient(180deg,#3fa6c8 0%,#1d6f92 55%,#2d4f50 100%)}
.photo-fish{background:
  radial-gradient(ellipse 140px 60px at 45% 92%,#8a6a3c,transparent 75%),
  radial-gradient(circle at 60% 30%,rgba(150,220,240,.55),transparent 40%),
  linear-gradient(180deg,#2f8fb8 0%,#17608a 55%,#123f55 100%)}
.event p{margin-top:33px;color:var(--grey-text);font-size:14px;line-height:23px}
.e1{left:55px}.e2{left:430px}.e3{left:805px}

/* see section */
.see-photo{top:2380px;height:640px;background:
  linear-gradient(180deg,rgba(80,120,100,.55) 0 120px,transparent 200px),
  radial-gradient(ellipse 420px 180px at 300px 520px,rgba(170,160,60,.28),transparent 70%),
  radial-gradient(ellipse 500px 200px at 900px 300px,rgba(90,170,190,.35),transparent 70%),
  linear-gradient(175deg,#3a7484 0%,#1f5566 40%,#133a48 100%)}
.see{top:2470px;height:460px;z-index:6}
.see h2{position:absolute;left:50px;top:26px;font-size:66px;line-height:72px}
.see h2 .thin{font-weight:100;display:block;color:rgba(255,255,255,.7)}
.see h2 .bold{font-weight:900;display:block}
.see .col{position:absolute;top:205px;width:540px}
.see .btn-red{left:50px;top:358px}

/* map */
.map{top:2930px;height:370px;background:linear-gradient(180deg,#303030,#272727);clip-path:polygon(0 75px,100% 0,100% 370px,0 370px);z-index:7}
.map-pin{position:absolute;left:620px;top:132px}

/* footer */
.site-footer{top:3297px;height:492px;background:var(--footer)}
.footer-col{position:absolute;top:90px}
.footer-col h4{font-size:22px;font-weight:900;margin-bottom:22px}
.footer-col li{list-style:none;font-size:14px;line-height:35px;color:var(--footer-text)}
.fc-about{left:50px}.fc-events{left:333px}
.footer-note{position:absolute;left:614px;top:166px;width:470px;font-size:11px;line-height:16px;color:var(--footer-text)}
.social{position:absolute;left:614px;top:262px;display:flex;gap:12px}
.social span{width:60px;height:60px;border-radius:50%;border:2px solid var(--white);display:flex;align-items:center;justify-content:center}
.copyright{position:absolute;left:614px;top:396px;font-size:11px;color:var(--footer-text)}
</style>
</head>
<body>

<div class="layer hero-photo" role="img" aria-label="Photo of a snorkeler swimming in clear blue water"></div>
<header class="site-header">
  <div class="brand">Brinewardsea.com</div>
  <nav class="main-nav">
    <a class="active" href="#">HOME</a>
    <a class="hover-mark" href="#">ABOUT</a>
    <a href="#">EVENTS</a>
    <a href="#">GALLERY</a>
    <a href="#">CONTACTS</a>
  </nav>
</header>
<div class="slider-arrows">
  <svg width="20" height="30" viewBox="0 0 20 30"><path d="M15 4 L5 15 L15 26" fill="none" stroke="#fff" stroke-width="4"/></svg>
  <svg width="20" height="30" viewBox="0 0 20 30"><path d="M5 4 L15 15 L5 26" fill="none" stroke="#fff" stroke-width="4"/></svg>
</div>

<section class="layer intro">
  <h1><span class="thin">FIND THE TREASURES OF</span><span class="bold">THE UNDERWATER WORLD</span></h1>
  <p class="col col-left">Lorem ipsum dolor sit amet conse ctetur adipisicing elit, sed do eiusmod tempor incididunt ut labore et dolore magna aliqua. Ut enim ad minim veniam, quis nostrud exercitation ullamco laboris nisi ut aliquip ex ea commodo consequat. Duis aute irure dolor in reprehenderit in voluptate velit esse cillum dolore eu fugiat nulla pariatur.</p>
  <p class="col col-right">Dolor sit amet conse ctetur adipisicing elit, sed do eiusmod tempor incididunt ut labore et dolore magna aliqua. Ut enim ad minim veniam, quis nostrud exercitation ullamco laboris nisi ut aliquip ex ea commodo consequat. Duis aute irure dolor in reprehenderit in voluptate velit esse cillum dolore eu fugiat nulla pariatur.</p>
  <a class="btn btn-dark">READ MORE</a>
</section>

<div class="layer about-photo" role="img" aria-label="Underwater photo of divers over a reef"></div>
<div class="layer about-dark"></div>
<section class="layer about">
  <h2 class="section-title">ABOUT <span class="thin">OUR CLUB</span></h2>
  <div class="feature f1"><div class="num">01</div><h3>LOREM IPSUM DOLOR SIT AMET CTETUR ADIPISICING ELIT</h3><p>Lorem ipsum dolor sit amet conse ctetur adipisicing elit, sed do eiusmod tempor incididunt ut labore et dolore magna aliqua. Ut enim ad minim veniam, quis nostrud exercitation ullamco.</p></div>
  <div class="feature f2"><div class="num">02</div><h3>NON PROIDENT, SUNT IN BR CULPA</h3><p>Lorem ipsum dolor sit amet conse ctetur adipisicing elit, sed do eiusmod tempor incididunt ut labore et dolore magna aliqua. Ut enim ad minim veniam, quis nostrud exercitation ullamco.</p></div>
  <div class="feature f3"><div class="num">03</div><h3>EXCEPTEUR SINT OCC AECAT CUPIDATAT</h3><p>Lorem ipsum dolor sit amet conse ctetur adipisicing elit, sed do eiusmod tempor incididunt ut labore et dolore magna aliqua. Ut enim ad minim veniam, quis nostrud exercitation ullamco.</p></div>
  <div class="feature f4"><div class="num">04</div><h3>QUI OFFICIA DESERUNT MOLLIT ANIM ID EST LABORUM</h3><p>Lorem ipsum dolor sit amet conse ctetur adipisicing elit, sed do eiusmod tempor incididunt ut labore et dolore magna aliqua. Ut enim ad minim veniam, quis nostrud exercitation ullamco.</p></div>
</section>

<section class="layer events">
  <h2 class="section-title"><span class="thin">OUR</span> EVENTS</h2>
  <div class="event e1"><div class="photo photo-surface" role="img" aria-label="Round photo of snorkelers at the surface"></div><p>Lorem ipsum dolor sit amet conse ctetur adipisicing elit, sed do eiusmod tempor incididunt ut labore et dolore magna aliqua. Ut enim ad minim veniam, quis nostrud exercitation.</p></div>
  <div class="event e2"><div class="photo photo-reef" role="img" aria-label="Round photo of a diver above coral"></div><p>Lorem ipsum dolor sit amet conse ctetur adipisicing elit, sed do eiusmod tempor incididunt ut labore et dolore magna aliqua. Ut enim ad minim veniam, quis nostrud exercitation.</p></div>
  <div class="event e3"><div class="photo photo-fish" role="img" aria-label="Round photo of a snorkeler with reef fish"></div><p>Lorem ipsum dolor sit amet conse ctetur adipisicing elit, sed do eiusmod tempor incididunt ut labore et dolore magna aliqua. Ut enim ad minim veniam, quis nostrud exercitation.</p></div>
</section>

<div class="layer see-photo" role="img" aria-label="Photo of divers at the water surface near a tropical shore"></div>
<section class="layer see">
  <h2><span class="thin">SEE THE UNDERWATER WORLD</span><span class="bold">WITH YOUR OWN EYES</span></h2>
  <p class="col col-left">Lorem ipsum dolor sit amet conse ctetur adipisicing elit, sed do eiusmod tempor incididunt ut labore et dolore magna aliqua. Ut enim ad minim veniam, quis nostrud exercitation ullamco laboris nisi ut aliquip ex ea commodo consequat. Duis aute irure dolor in reprehenderit in voluptate velit esse cillum dolore eu fugiat nulla pariatur.</p>
  <p class="col col-right">Dolor sit amet conse ctetur adipisicing elit, sed do eiusmod tempor incididunt ut labore et dolore magna aliqua. Ut enim ad minim veniam, quis nostrud exercitation ullamco laboris nisi ut aliquip ex ea commodo consequat. Duis aute irure dolor in reprehenderit in voluptate velit esse cillum dolore eu fugiat nulla pariatur.</p>
  <a class="btn btn-red">READ MORE</a>
</section>

<div class="layer map" role="img" aria-label="Dark street map showing the club location">
  <svg class="map-pin" width="34" height="52" viewBox="0 0 34 52"><path d="M17 2 C8 2 2 9 2 17 C2 29 17 50 17 50 C17 50 32 29 32 17 C32 9 26 2 17 2 Z" fill="#e8484e"/><circle cx="17" cy="17" r="6" fill="#2b2b2b"/></svg>
</div>

<footer class="layer site-footer">
  <div class="footer-col fc-about"><h4>ABOUT</h4><ul>
    <li>Lorem ipsum dolor sit amet</li><li>Conse ctetur adipisicing</li><li>Elit sed do eiusmod tempor</li><li>Incididunt ut labore</li><li>Et dolore magna aliqua</li><li>Ut enim ad minim veniam</li><li>Quis nostrud exercitation</li><li>Ullamco laboris n</li></ul></div>
  <div class="footer-col fc-events"><h4>EVENTS</h4><ul>
    <li>Conse ctetur adipisicing</li><li>Elit sed do eiusmod tempor</li><li>Incididunt ut labore</li><li>Et dolore magna aliqua</li><li>Ut enim ad minim veniam</li><li>Quis nostrud exercitation</li><li>Ullamco laboris n</li></ul></div>
  <p class="footer-note">Lorem ipsum dolor sit amet conse ctetur adipisicing elit, sed do eiusmod tempor incididunt ut labore et dolore magna aliqua. Ut enim ad minim veniam, quis nostrud exercitation ullamco laboris nisi ut aliquip ex ea commodo consequat. Duis aute irure dolor in reprehenderit in voluptate velit esse cillum dolore eu fugiat nulla pariatur.</p>
  <div class="social" aria-label="Contact links">
    <span aria-label="Phone"><svg width="24" height="24" viewBox="0 0 24 24"><path d="M6.6 10.8a15 15 0 0 0 6.6 6.6l2.2-2.2c.3-.3.7-.4 1-.2 1.1.4 2.3.6 3.6.6.6 0 1 .4 1 1V20c0 .6-.4 1-1 1A17 17 0 0 1 3 4c0-.6.4-1 1-1h3.5c.6 0 1 .4 1 1 0 1.3.2 2.5.6 3.6.1.3 0 .7-.2 1z" fill="#fff"/></svg></span>
    <span aria-label="Email"><svg width="26" height="20" viewBox="0 0 26 20"><rect x="2" y="2" width="22" height="16" rx="2" fill="none" stroke="#fff" stroke-width="2.4"/><path d="M3 4 L13 11 L23 4" fill="none" stroke="#fff" stroke-width="2.4"/></svg></span>
    <span aria-label="Location"><svg width="20" height="28" viewBox="0 0 34 52"><path d="M17 2 C8 2 2 9 2 17 C2 29 17 50 17 50 C17 50 32 29 32 17 C32 9 26 2 17 2 Z" fill="#fff"/><circle cx="17" cy="17" r="6" fill="#1c1c1c"/></svg></span>
  </div>
  <p class="copyright">Brinewardsea © 2016 Privacy Policy</p>
</footer>

</body>
</html>
```